Cover Design For eBook "Quill"

I need two e-book covers with the same look and feel:

first one:
title
THE QUILL MOVEMENT
subtitle
WIDEN ONLINE SUPPORT
author
MAPLEWAY GIFTS (just include the logo I attach)

second eBook
title
THE QUILL METHOD
subtitle
5 STEPS TO WIDEN YOUR CHURCH'S ONLINE SUPPORT
author
MAPLEWAY GIFTS (just include the log I attach)

Industry/Entity Type

Digital

Colors
f04a50
f68e4e
faa54b
ffcf3e

Requirements
Must have
• the MAPLEWAY GIFTS LOGO I attached at the bottom of the design.
• There needs to be some type of spark coming off of one of the letters in QUILL
Nice to have
• I'd love to have a horizontal and vertical layout

```html
<!DOCTYPE html>
<html lang="en">
<head>
<meta charset="utf-8">
<title>The Quill Method – eBook Cover</title>
<link href="https://fonts.googleapis.com/css2?family=Antonio:wght@400;700&family=Permanent+Marker&display=swap" rel="stylesheet">
<style>
  :root {
    --paper-orange: #f39a2c;
    --paper-orange-light: #f8ad45;
    --paper-orange-deep: #e9831f;
    --title-grey: #8d9096;
    --title-grey-dark: #4f5257;
    --quill-light: #d9dadd;
    --quill-dark: #7c7f85;
    --ink-black: #111111;
    --brand-red: #f04a50;
    --brand-grey: #3c3f44;
  }
  html, body {
    margin: 0;
    padding: 0;
    overflow: hidden;
    background: #ffffff;
  }
  .cover {
    position: relative;
    width: 750px;
    height: 1200px;
    overflow: hidden;
  }
  .cover-background {
    position: absolute;
    inset: 0;
    background: radial-gradient(ellipse at 50% 40%, var(--paper-orange-light) 0%, var(--paper-orange) 55%, var(--paper-orange-deep) 100%);
  }
  .title {
    position: absolute;
    inset: 0;
    margin: 0;
    text-align: center;
    font-family: "Permanent Marker", "Marker Felt", cursive;
    font-weight: 400;
    color: var(--title-grey);
    line-height: 1;
    text-shadow:
      2px 2px 0 var(--title-grey-dark),
      4px 5px 6px rgba(0, 0, 0, 0.45);
  }
  .title-line {
    position: absolute;
    left: 0;
    right: 0;
    display: block;
  }
  .title-line--the { top: 80px; font-size: 140px; letter-spacing: 6px; }
  .title-line--quill { top: 300px; font-size: 160px; letter-spacing: 4px; }
  .title-line--method { top: 490px; font-size: 140px; letter-spacing: 2px; }

  .quill-feather {
    position: absolute;
    left: 600px;
    top: 215px;
    width: 26px;
    height: 120px;
    border-radius: 50% 50% 40% 40%;
    background: linear-gradient(180deg, var(--quill-light), var(--quill-dark));
    transform: rotate(28deg);
    transform-origin: bottom center;
  }

  .subtitle,
  .brand {
    position: absolute;
    left: 0;
    top: 0;
    width: 750px;
    height: 1200px;
    margin: 0;
  }
  .subtitle-text {
    font-family: "Antonio", sans-serif;
    font-weight: 400;
    font-size: 112px;
    fill: var(--ink-black);
  }
  .brand-mark { fill: var(--brand-red); }
  .brand-name {
    font-family: "Antonio", sans-serif;
    font-weight: 700;
    font-size: 64px;
    fill: var(--brand-grey);
  }
</style>
</head>
<body>
  <main class="cover">
    <div class="cover-background" role="img" aria-label="Orange paper texture with scattered white sparkle glints"></div>

    <h1 class="title">
      <span class="title-line title-line--the">THE</span>
      <span class="title-line title-line--quill">QUILL</span>
      <span class="title-line title-line--method">METHOD</span>
    </h1>

    <div class="quill-feather" role="img" aria-label="Quill feather rising from the last letter of QUILL"></div>

    <svg class="subtitle" viewBox="0 0 750 1200" role="img" aria-label="5 STEPS TO WIDEN YOUR CHURCH'S ONLINE SUPPORT">
      <text class="subtitle-text" x="45" y="802" textLength="652" lengthAdjust="spacingAndGlyphs">5 STEPS TO WIDEN YOUR</text>
      <text class="subtitle-text" x="45" y="952" textLength="660" lengthAdjust="spacingAndGlyphs">CHURCH'S ONLINE SUPPORT</text>
    </svg>

    <svg class="brand" viewBox="0 0 750 1200" role="img" aria-label="MAPLEWAY GIFTS">
      <circle class="brand-mark" cx="57" cy="1103" r="42"/>
      <text class="brand-name" x="128" y="1128" textLength="595" lengthAdjust="spacingAndGlyphs">MAPLEWAY GIFTS</text>
    </svg>
  </main>
</body>
</html>
```